Professional website for software / consulting firm targeting the legal market.
Veranth Systems
Professional website for software / consulting firm targeting the legal market. - Software
Creative Brief
Software
www.veranth.example
The company provides consulting to law firms engaged in mass tort litigation with expertise in data mining and analysis, e-discovery and case management. The company is also engaged in software development with focus on e-discovery collection and analysis.
Like professional looking, easy to navigate websites that aren't cluttered or cumbersome yet informative and efficient.
below header
As we work primarily in the legal space we need to portray our professional, focused image equally coupled with our modern, technology focus bent on problem solving.
kmorlen kmorlen
In addition, I want to clarify our consulting offerings and software. We are focusing on providing software solutions to empower our clients to solve their business challenges. Our brand of consulting doesn't stop at identifying the problem but continues to finding a solution and then implementing the solution. We want to truly focus on our ability to understand the issues and development software solutions for our industry. I hope this helps in your design efforts.
Thank you to all the designers working on this project. Here are my evolving thoughts: 1. Go lighter on written content on the homepage. Information which pertains to About us, services, products and contact us will be placed on those interior pages. With the exception of an info@veranth.example and phone number which should always be available regardless of page. 2. Search features are not needed 3. Client list will not be made available nor highlighted 4. I am leaning towards those designs which are clean and highly professional looking with a tech edge. 5. I like the large initial photo banner which scrolls through several images with tag lines. These remind me of mini-advertisements which need to convey a pointed message in 1 line of words with a good photo.
The tabs for the interior pages on the navigation should be: Home | About Us | Products | Services Please try to keep the landing page design for the homepage to a single page. We would like to keep a clean design with minimal scrolling on information pages. A common theme in the designs is the use of the rotating banners which I like very much and think these are a good way to provide varying pieces of information without having the end user having to scroll down a page. Thank you for the work thus far, I will attempt to provide feedback as quickly as possible on submitted designs.

```html
<!DOCTYPE html>
<html lang="en">
<head>
<meta charset="utf-8">
<title>Veranth Systems</title>
<link href="https://fonts.googleapis.com/css2?family=Arvo:wght@700&family=Open+Sans:wght@400;600;700&display=swap" rel="stylesheet">
<style>
:root{
  --navy:#0e2a4f;
  --navy-deep:#0b2140;
  --blue:#1a6fa8;
  --blue-bright:#2a86c2;
  --grey-bg:#e8eaec;
  --tile-grey:#6b6f74;
  --orange:#f0a316;
  --text:#333a42;
  --footer-text:#8fa6c3;
  --link:#2a86c2;
  --green:#6aa82c;
  --white:#ffffff;
}
*{box-sizing:border-box;margin:0;padding:0}
html,body{width:1200px;height:869px;overflow:hidden}
body{font-family:"Open Sans",Arial,sans-serif;color:var(--text);background:var(--white);position:relative}

.site-header{position:absolute;top:0;left:0;width:1200px;height:79px;background:var(--white)}
.brand{position:absolute;left:180px;top:18px;display:flex;align-items:center;gap:10px}
.brand-mark{width:34px;height:34px;border-radius:50%;background:var(--navy)}
.brand-name{font-weight:700;font-size:28px;color:var(--navy);letter-spacing:.5px}
.social{position:absolute;right:168px;top:32px;display:flex;gap:5px}
.social span{width:22px;height:22px;border-radius:3px;display:block}
.social .s1{background:#d9472b}.social .s2{background:#35a9e0}.social .s3{background:#3b5a9a}.social .s4{background:#1b78b5}

.main-nav{position:absolute;left:173px;top:79px;width:854px;height:36px;background:linear-gradient(var(--blue),var(--navy));display:flex;align-items:center;padding-left:14px}
.main-nav a{color:var(--white);text-decoration:none;font-size:12px;font-weight:600;padding:0 18px;height:36px;line-height:36px}
.main-nav a.active{border-bottom:3px solid var(--white)}
.search{position:absolute;right:6px;top:7px;display:flex}
.search-field{width:150px;height:22px;background:var(--white);border:1px solid #ccc;font-size:10px;color:#999;padding:4px 6px}
.search-btn{height:22px;background:var(--orange);color:var(--white);font-size:10px;font-weight:700;padding:4px 9px}

.hero{position:absolute;left:0;top:115px;width:1200px;height:365px;background:var(--grey-bg);overflow:hidden}
.hero-curve{position:absolute;left:0;top:0}
.hero-copy{position:absolute;left:175px;top:56px;width:360px;color:var(--white)}
.hero-copy h1{font-family:"Arvo",Georgia,serif;font-weight:700;font-size:41px;line-height:44px}
.hero-copy p{font-size:13px;line-height:17px;margin-top:18px;width:310px}
.hero-visual{position:absolute;left:640px;top:50px;width:430px;height:315px;border-radius:16px 16px 0 0;background:linear-gradient(160deg,#2e3236 0%,#5d666e 45%,#a9b2b8 75%,#e2c7ac 100%)}
.more-btn{position:absolute;left:233px;top:295px;width:122px;height:122px;border-radius:50%;background:var(--orange);border:4px solid var(--white);color:var(--white);font-size:13px;text-align:center;padding-top:26px;line-height:16px}

.welcome{position:absolute;left:174px;top:508px;width:320px}
.welcome h2{font-size:25px;font-weight:400;color:var(--text);letter-spacing:1px}
.welcome h2 span{color:var(--navy);font-weight:700}
.welcome p{font-size:11.5px;line-height:15px;margin-top:12px;color:var(--text)}
.welcome p b{color:var(--link);font-weight:600}

.process{position:absolute;left:511px;top:523px;display:flex}
.tile{width:128.5px;height:130px;display:flex;flex-direction:column;align-items:center;padding-top:14px;color:var(--white);font-size:10px;font-weight:600;text-align:center;line-height:12px}
.tile:nth-child(1),.tile:nth-child(3){background:var(--tile-grey)}
.tile:nth-child(2){background:var(--navy)}
.tile:nth-child(4){background:var(--blue-bright)}
.tile svg{margin-bottom:8px}

.site-footer{position:absolute;left:0;top:686px;width:1200px;height:183px;background:var(--navy)}
.footer-cols{position:absolute;left:174px;top:18px;display:flex}
.col h3{font-size:12px;font-weight:600;color:var(--white);margin-bottom:8px}
.col a{display:block;font-size:10px;color:var(--footer-text);line-height:14px;text-decoration:none}
.col-company{width:135px}.col-service{width:235px}
.col-service .links{display:grid;grid-template-columns:85px 135px}
.col-account{width:128px}.col-follow{width:120px}
.follow-row{display:flex;gap:4px}
.follow-row span{width:20px;height:20px;border-radius:3px;display:block}
.col-news p{font-size:10px;color:var(--footer-text);line-height:13px;width:170px}
.news-field{width:170px;height:20px;background:var(--white);margin-top:6px}
.news-btn{display:inline-block;margin-top:8px;background:var(--green);color:var(--white);font-size:10px;font-weight:700;padding:4px 8px;border-radius:2px}
.copyright{position:absolute;left:0;bottom:0;width:1200px;height:41px;background:var(--navy-deep);color:var(--footer-text);font-size:10px;text-align:center;line-height:41px}
</style>
</head>
<body>
<header class="site-header">
  <div class="brand"><span class="brand-mark"></span><span class="brand-name">Veranth Systems</span></div>
  <div class="social"><span class="s1"></span><span class="s2"></span><span class="s3"></span><span class="s4"></span></div>
</header>

<nav class="main-nav">
  <a class="active">HOME</a><a>ABOUT US</a><a>PRODUCTS</a><a>SERVICES</a><a>CONTACT US</a>
  <div class="search"><div class="search-field">Enter your address</div><div class="search-btn">SEARCH</div></div>
</nav>

<section class="hero">
  <div class="hero-visual" role="img" aria-label="Photo of hands holding a tablet showing a web application"></div>
  <svg class="hero-curve" width="560" height="365" viewBox="0 0 560 365">
    <defs><linearGradient id="heroBlue" x1="0" y1="0" x2="1" y2="1"><stop offset="0" stop-color="#2a86c2"/><stop offset="1" stop-color="#145c93"/></linearGradient></defs>
    <path d="M0 0H520Q600 182 520 365H0Z" fill="#ffffff"/>
    <path d="M0 0H508Q585 182 508 365H0Z" fill="url(#heroBlue)"/>
  </svg>
  <div class="hero-copy">
    <h1>It’s time for<br>ediscovery<br>to transform.</h1>
    <p>The company provides consulting to law firms engaged in mass tort litigation with expertise in data mining and analysis, e-discovery and case management.</p>
  </div>
  <div class="more-btn">MORE<br>DETAILS</div>
</section>

<section class="welcome">
  <h2>WELCOME TO <span>VERANTH</span></h2>
  <p>Lorem ipsum dolor sit amet, consectetur adipisicing elit, sed do eiusmod tempor incididunt ut labore et dolore magna aliqua. Ut enim ad minim veniam, quis nostrud exercitation ullamco laboris nisi ut aliquip ex ea commodo consequat. Duis aute irure dolor in reprehenderit in voluptate velit esse <b>cillum dolore eu fugiat</b> nulla pariatur.</p>
</section>

<section class="process">
  <div class="tile">
    <svg width="62" height="62" viewBox="0 0 62 62"><circle cx="31" cy="31" r="29" fill="#4a4e53" stroke="#fff" stroke-width="2"/><rect x="18" y="20" width="26" height="18" fill="none" stroke="#fff" stroke-width="2.5"/><path d="M27 25l8 4-8 4z" fill="#fff"/><path d="M24 44h14" stroke="#fff" stroke-width="2.5"/></svg>
    LEGAL HOLD</div>
  <div class="tile">
    <svg width="62" height="62" viewBox="0 0 62 62"><circle cx="31" cy="31" r="29" fill="#fff"/><circle cx="30" cy="27" r="11" fill="none" stroke="#0e2a4f" stroke-width="3"/><path d="M26 40h8M27 44h6" stroke="#0e2a4f" stroke-width="3"/></svg>
    IDENTIFICATION &amp;<br>COLLECTION</div>
  <div class="tile">
    <svg width="62" height="62" viewBox="0 0 62 62"><circle cx="31" cy="31" r="29" fill="#4a4e53" stroke="#fff" stroke-width="2"/><circle cx="31" cy="31" r="11" fill="none" stroke="#fff" stroke-width="3"/><circle cx="31" cy="31" r="4" fill="#fff"/><path d="M31 15v5M31 42v5M15 31h5M42 31h5" stroke="#fff" stroke-width="3"/></svg>
    PROCESSING &amp;<br>ANALYSIS</div>
  <div class="tile">
    <svg width="62" height="62" viewBox="0 0 62 62"><circle cx="31" cy="31" r="29" fill="#fff"/><rect x="20" y="17" width="20" height="26" fill="none" stroke="#2a86c2" stroke-width="2.5"/><path d="M24 24h12M24 30h12M24 36h7" stroke="#2a86c2" stroke-width="2"/><path d="M36 44l10-14" stroke="#2a86c2" stroke-width="3"/></svg>
    REVIEW &amp;<br>PRODUCTION</div>
</section>

<footer class="site-footer">
  <div class="footer-cols">
    <div class="col col-company"><h3>COMPANY LINK</h3><a>About Us</a><a>Contact Us</a><a>Bookmark Us</a></div>
    <div class="col col-service"><h3>CUSTOMER SERVICES</h3>
      <div class="links"><a>About Us</a><a>Shipping</a><a>Terms of Use</a><a>Returns Product Index</a><a>Privacy Policy</a><a>Category Index</a><a>Shipping</a></div></div>
    <div class="col col-account"><h3>MY ACCOUNT</h3><a>My Account</a><a>Site Map</a></div>
    <div class="col col-follow"><h3>FOLLOW US</h3>
      <div class="follow-row"><span style="background:#3b5a9a"></span><span style="background:#35a9e0"></span><span style="background:#d9472b"></span><span style="background:#1b78b5"></span></div></div>
    <div class="col col-news"><h3>NEWSLETTER</h3><p>Sign up for our newsletter to get the latest news and updates</p><div class="news-field"></div><span class="news-btn">Subscribe Now!</span></div>
  </div>
  <div class="copyright">Copyright © 2014 veranth.example. All Rights Reserved.</div>
</footer>
</body>
</html>
```